Presentation Folder

We are looking for a presentation folder design that will allow us to bring our proposals/quotes to clients and leave with them. The front cover should have our logo as well as show some of the products we sell: IT Networking equipment, WiFi, Servers/Storage.
Inside flap has an area for our business cards.

Target Market(s)

Mid Sized Businesses and Private Education. Business to Business. IT Directors. Ages 30 to 50. College Educated. Southern California

Industry/Entity Type

Business

Logo Text

Requirements
Must have
• Our Logo
Complimentary color schemes to our logo.
Should be Professional.

```html
<!DOCTYPE html>
<html lang="en">
<head>
<meta charset="utf-8">
<title>Kestra IT – Presentation Folder</title>
<link rel="stylesheet" href="https://fonts.googleapis.com/css2?family=Montserrat:wght@300;400;600&display=swap">
<style>
  :root {
    --stage: #e4e4e4;
    --cover-blue: #0f7fa5;
    --back-cyan: #00b1e1;
    --band-grey: #d9dadb;
    --pocket-charcoal: #3e3e40;
    --pocket-orange: #e6792a;
    --inner-white: #f7f7f7;
    --inner-grey: #cfd0d2;
    --accent: #2fc1ee;
    --ink: #ffffff;
    --ink-dark: #5a5a5c;
    --card-ink: #d6d6d6;
    --card-bg: #2d2d2f;
  }
  * { box-sizing: border-box; margin: 0; padding: 0; }
  html, body { width: 1200px; height: 847px; overflow: hidden; }
  body {
    background: var(--stage);
    font-family: "Montserrat", sans-serif;
    display: flex; align-items: center; justify-content: center; gap: 60px;
  }
  .spread { display: flex; box-shadow: 0 10px 30px rgba(0,0,0,.18); }
  .panel { width: 270px; height: 360px; position: relative; overflow: hidden; }
  .wordmark { font-weight: 300; letter-spacing: 1px; white-space: nowrap; line-height: 1; }

  /* Outside: back cover */
  .back-cover { background: var(--back-cyan); }
  .back-footer {
    position: absolute; left: 0; right: 0; bottom: 28px; height: 54px;
    background: #fff; display: flex; align-items: center; gap: 8px; padding-left: 16px;
  }
  .back-footer .wordmark { font-size: 17px; color: var(--ink-dark); }
  .hq-details { font-size: 5px; line-height: 1.35; color: var(--ink-dark); }

  /* Outside: front cover */
  .front-cover { background: var(--cover-blue); }
  .front-cover .wordmark {
    position: absolute; top: 50px; right: 18px; font-size: 24px; color: var(--ink);
  }
  .product-band {
    position: absolute; left: 0; right: 0; top: 186px; height: 48px; background: var(--band-grey);
  }
  .product { position: absolute; top: 168px; height: 58px; border-radius: 4px; }
  .product-server { left: 8px; width: 72px; background: linear-gradient(#c9cbce, #7c7f84); }
  .product-wifi { left: 100px; width: 64px; background: linear-gradient(#f1f0ea, #c8c6bd); border-radius: 10px; }
  .product-board { left: 188px; width: 58px; border-radius: 50%; background: radial-gradient(#6f8a6a, #2f4430); }
  .front-cover .guides { position: absolute; inset: 0; }

  /* Inside spread */
  .inside-left { background: var(--inner-white); }
  .inside-right { background: var(--inner-grey); }
  .pocket {
    position: absolute; left: 0; right: 0; bottom: 0; height: 90px;
    display: flex; align-items: center; justify-content: center;
  }
  .pocket-charcoal { background: var(--pocket-charcoal); }
  .pocket-charcoal .wordmark { font-size: 26px; color: #9c9c9e; }
  .pocket-orange { background: var(--pocket-orange); }
  .business-card {
    width: 110px; height: 58px; background: var(--card-bg); border-radius: 2px;
    padding: 7px 8px; color: #fff;
  }
  .business-card .wordmark { font-size: 11px; display: block; margin-bottom: 5px; }
  .business-card .card-details { font-size: 4.6px; line-height: 1.4; color: var(--card-ink); }
</style>
</head>
<body>

  <section class="spread outside-spread" aria-label="Folder outside">
    <div class="panel back-cover">
      <div class="back-footer">
        <span class="wordmark">KESTRA IT</span>
        <p class="hq-details">Corporate Headquarters<br>2410 Harbor Way, Ste 204<br>Seaside Bay, CA 90000<br>555-014-2280<br>www.kestrait.example</p>
      </div>
    </div>

    <div class="panel front-cover">
      <span class="wordmark">KESTRA IT</span>
      <div class="product-band"></div>
      <svg class="guides" width="270" height="360" viewBox="0 0 270 360" aria-hidden="true">
        <line x1="90" y1="140" x2="90" y2="186" stroke="var(--accent)" stroke-width="1"/>
        <circle cx="90" cy="140" r="2" fill="var(--accent)"/>
        <line x1="176" y1="234" x2="176" y2="280" stroke="var(--accent)" stroke-width="1"/>
        <circle cx="176" cy="280" r="2" fill="var(--accent)"/>
      </svg>
      <div class="product product-server" role="img" aria-label="Photo of rack-mounted servers and storage units"></div>
      <div class="product product-wifi" role="img" aria-label="Photo of a ceiling WiFi access point"></div>
      <div class="product product-board" role="img" aria-label="Photo of a networking circuit board"></div>
    </div>
  </section>

  <section class="spread inside-spread" aria-label="Folder inside">
    <div class="panel inside-left">
      <div class="pocket pocket-charcoal">
        <span class="wordmark">KESTRA IT</span>
      </div>
    </div>
    <div class="panel inside-right">
      <div class="pocket pocket-orange">
        <div class="business-card">
          <span class="wordmark">KESTRA IT</span>
          <p class="card-details">2410 Harbor Way, Ste 204<br>Seaside Bay, CA 90000<br>555-014-2280<br>www.kestrait.example</p>
        </div>
      </div>
    </div>
  </section>

</body>
</html>
```